New Plumbing Company

We are looking for a smart and creative business card design for our new plumbing company. We are looking for creativity and originality in our business cards.

Industry/Entity Type

Plumbing

Contact Information for Business Card

Crestline Plumbing
Peter Halvane
Managing Director
Telephone Number : 0481529604
Email : service@crestlineplumbing.com.au
Website : www.crestlineplumbing.com.au
Lic. 508264K

Colors
0692cd
33a6d7
000000

Requirements
Must have
• I want the business card to be designed on a black background using the blue tones i have selected as seen in the company logo.

```html
<!DOCTYPE html>
<html lang="en">
<head>
<meta charset="utf-8">
<title>Crestline Plumbing – Business Card</title>
<link href="https://fonts.googleapis.com/css2?family=Lato:wght@300;400&display=swap" rel="stylesheet">
<style>
  :root {
    --backdrop: #3d3d3d;
    --card-light: #f3f3f3;
    --card-dark: #000000;
    --brand-blue: #0692cd;
    --accent-blue: #1a78c2;
    --ink: #2e2e2e;
    --paper-white: #ffffff;
  }
  * { margin: 0; padding: 0; box-sizing: border-box; }
  html, body {
    width: 1200px;
    height: 900px;
    overflow: hidden;
    background: var(--backdrop);
    font-family: "Lato", sans-serif;
  }
  .canvas { position: relative; width: 1200px; height: 900px; }
  .card {
    position: absolute;
    top: 184px;
    width: 302px;
    height: 490px;
    border-radius: 12px;
    text-align: center;
  }
  .card--front { left: 298px; background: var(--card-light); color: var(--ink); }
  .card--back { left: 646px; background: var(--card-dark); color: var(--paper-white); }

  .brand-mark {
    position: absolute;
    top: 70px;
    left: 0;
    width: 100%;
    display: flex;
    flex-direction: column;
    align-items: center;
    gap: 14px;
  }
  .brand-mark__dot {
    width: 46px;
    height: 46px;
    border-radius: 50%;
    background: var(--brand-blue);
  }
  .brand-mark__name {
    font-size: 20px;
    font-weight: 400;
    color: var(--brand-blue);
    letter-spacing: 0.5px;
  }

  .person { position: absolute; top: 226px; left: 0; width: 100%; }
  .person__name {
    font-size: 22px;
    font-weight: 400;
    color: var(--accent-blue);
    letter-spacing: 0.4px;
    line-height: 28px;
  }
  .person__role { font-size: 14px; line-height: 20px; margin-left: 4px; }

  .contact {
    position: absolute;
    top: 310px;
    left: 0;
    width: 100%;
    list-style: none;
    font-size: 14px;
    line-height: 20px;
  }
  .contact__item { display: flex; justify-content: center; align-items: center; gap: 7px; }
  .contact__item--phone { margin-left: 4px; }
  .contact__icon { width: 10px; height: 10px; fill: var(--accent-blue); }

  .licence { position: absolute; top: 400px; left: 0; width: 100%; font-size: 14px; }

  .wordmark {
    position: absolute;
    top: 222px;
    left: 0;
    width: 100%;
    font-size: 28px;
    font-weight: 300;
    letter-spacing: 0.5px;
    color: var(--paper-white);
  }
  .website {
    position: absolute;
    top: 434px;
    left: 0;
    width: 100%;
    font-size: 13px;
    letter-spacing: 0.2px;
  }
</style>
</head>
<body>
<main class="canvas">
  <section class="card card--front" aria-label="Card front">
    <div class="brand-mark">
      <span class="brand-mark__dot"></span>
      <span class="brand-mark__name">Crestline Plumbing</span>
    </div>
    <div class="person">
      <h1 class="person__name">PETER HALVANE</h1>
      <p class="person__role">Managing Director</p>
    </div>
    <ul class="contact">
      <li class="contact__item contact__item--phone">
        <svg class="contact__icon" viewBox="0 0 10 10" aria-hidden="true">
          <path d="M1 3 Q5 0 9 3 L8 4.5 L6.5 3.8 L6.5 3 Q5 2.6 3.5 3 L3.5 3.8 L2 4.5 Z M2.5 5 L7.5 5 L8.5 9 L1.5 9 Z"/>
        </svg>
        <span>0481529604</span>
      </li>
      <li class="contact__item">
        <svg class="contact__icon" viewBox="0 0 10 10" aria-hidden="true">
          <path d="M0.5 2 H9.5 V8 H0.5 Z" />
          <path d="M0.5 2 L5 5.5 L9.5 2" fill="none" stroke="#f3f3f3" stroke-width="0.9"/>
        </svg>
        <span>service@crestlineplumbing.com.au</span>
      </li>
    </ul>
    <p class="licence">Lic. 508264K</p>
  </section>

  <section class="card card--back" aria-label="Card back">
    <h2 class="wordmark">Crestline Plumbing</h2>
    <p class="website">www.crestlineplumbing.com.au</p>
  </section>
</main>
</body>
</html>
```